Mailer 001

https://www.filecrate.example/sh/x4k2pq7rtz19wmn/Lb3vQeNcRy
Orentation: Landscape
SIZE: 5 1/2' by 10 1/2'
COLORS: 32cd32, 13e613, 21f721, 00FE00, 00D800, 00B200, 009900

Re-Elect Dalton Pierce
Utah House of Representatives
Questions? Please call! (801) 555-0147

Text for side 1

Promises Made - Promises Kept
- Again I Promise to continue to advocate for limited government
- Again I Promise to advocate for educational choice
- Again I Promise to promote fiscal responsibility, transparency, and accountability.
- Again I Promise to take seriously my pledge to protect individual and economic liberty.

Text for side 2

Principled Conservative
I am committed to my oath to uphold the U.S. Constitution and Utah Constitution. As an attorney who has studied these documents, I understand the principles of federalism and of our republican form of government. I also understand that big government is a threat to our freedoms, even at the state and local levels. I have a record of sponsoring and supporting legislation that makes government more efficient and less burdensome.
- Dalton Pierce

Let’s finish what WE started
www.DaltonPierceHD42.example

Note: side 2 needs room for address lables as this will be a mailer sent out in the US post
, This is a mailer for a client of mine. It will be mailed out soon.
There is a filecrate link so you can look at some of the work done previously, the work done before was not done by a professional, but it will give you an idea of the branding style. Colors should match previous branding.

feel free to ask questions if needed.

Filecrate: https://www.filecrate.example/sh/x4k2pq7rtz19wmn/Lb3vQeNcRy
Orientation: Landscape
SIZE: 5 1/2' by 10 1/2'

Re-Elect Dalton Pierce

Text for side 1

Text for side 2

Principled Conservative
- Dalton Pierce

www.DaltonPierceHD42.example

If you are unable to get to the filecrate you and download a zip file.
https://docs.storevault.example/file/d/8ZqP2mWtR5xJ7LnYcK4bHsDvFgAe/edit?usp=sharing

Please note: we are looking for fresh and creative designs, not designs that look like the old flyers done by non-professionals.

Make the designs fresh and creative, I know that is an old a tired bit of instructions and ambiguous, so to clear that up a bit.....if the design look like I could have knocked I personally could have done, that is not what I want.  Do not just cut and paste images, use transparency, complementary colors and fading.  The design should be artistic.

bring your creativity and artistic nature.

```html
<!DOCTYPE html>
<html lang="en">
<head>
<meta charset="utf-8">
<title>Re-Elect Dalton Pierce – Mailer</title>
<link href="https://fonts.googleapis.com/css2?family=Archivo+Black&family=Anton&family=Roboto+Condensed:wght@400;700&family=PT+Sans:wght@400;700&family=PT+Serif:wght@700&display=swap" rel="stylesheet">
<style>
  :root {
    --lime: #00fe00;
    --green-bright: #21f721;
    --green-mid: #13e613;
    --green-brand: #32cd32;
    --green-deep: #00b200;
    --green-dark: #009900;
    --green-ink: #1a6e1a;
    --tag-green: #19c219;
    --white: #ffffff;
    --stage: #e6e6e6;
    --rule: #9a9a9a;
  }
  * { margin: 0; padding: 0; box-sizing: border-box; }
  html, body { width: 1200px; height: 1163px; overflow: hidden; background: var(--stage); }
  .canvas { position: relative; width: 1200px; height: 1163px; }

  .card { position: absolute; left: 79px; width: 1024px; height: 537px; overflow: hidden; background: var(--white); }
  .card--front { top: 26px; }
  .card--back { top: 599px; }

  /* Front */
  .front-field { position: absolute; inset: 0 0 117px 0;
    background: linear-gradient(180deg, var(--lime) 0%, var(--green-mid) 55%, var(--green-deep) 100%); }
  .capitol-photo { position: absolute; left: 194px; top: 30px; width: 240px; height: 390px;
    background: linear-gradient(180deg, rgba(0,120,0,0.35), rgba(0,150,0,0.25) 60%, rgba(0,120,0,0.2));
    border-radius: 110px 110px 0 0; }
  .candidate-photo { position: absolute; left: 0; top: 62px; width: 363px; height: 475px;
    background: linear-gradient(160deg, #d9b8a0 0%, #c79f86 28%, #5b8fd0 45%, #3f74bd 100%);
    border-radius: 160px 160px 0 0; }

  .headline { position: absolute; font-family: "Archivo Black", sans-serif; font-size: 42px; line-height: 1;
    color: var(--white); letter-spacing: 0.3px; text-shadow: 2px 2px 3px rgba(0,0,0,0.45); white-space: nowrap; }
  .headline--made { left: 392px; top: 62px; }
  .headline--kept { right: 42px; top: 125px; }

  .promise-lead { position: absolute; left: 383px; top: 208px; font-family: "Roboto Condensed", sans-serif;
    font-size: 30px; color: var(--white); text-shadow: 1px 1px 2px rgba(0,0,0,0.4); }
  .promise-list { position: absolute; left: 383px; top: 254px; list-style: none;
    font-family: "Roboto Condensed", sans-serif; font-size: 22px; line-height: 29px; color: var(--white);
    text-shadow: 1px 1px 2px rgba(0,0,0,0.5); white-space: nowrap; }

  .tagline { font-family: "Anton", sans-serif; color: var(--tag-green); white-space: nowrap; }
  .site { font-family: "Roboto Condensed", sans-serif; color: var(--green-deep); white-space: nowrap; }
  .card--front .tagline { position: absolute; left: 395px; top: 430px; font-size: 32px; line-height: 1; }
  .card--front .site { position: absolute; left: 395px; top: 483px; font-size: 28px; line-height: 1; }

  .brand-box { position: absolute; background: var(--green-brand); color: var(--white);
    font-family: "PT Serif", serif; font-weight: 700; white-space: nowrap; }
  .brand-row { display: flex; justify-content: space-between; align-items: baseline; }
  .brand-name { display: block; text-align: center; }
  .brand-office { display: block; text-align: right; }

  .card--front .brand-box { left: 787px; top: 426px; width: 212px; height: 102px; padding: 6px 10px; }
  .card--front .brand-row { font-size: 15px; line-height: 18px; }
  .card--front .brand-row .brand-first { font-size: 18px; }
  .card--front .brand-name { font-size: 36px; line-height: 40px; }
  .card--front .brand-office { font-size: 11px; line-height: 16px; }

  /* Back */
  .back-field { position: absolute; left: 0; top: 0; width: 543px; height: 537px;
    background: linear-gradient(180deg, var(--lime) 0%, var(--green-bright) 40%, var(--green-deep) 100%); }
  .capitol-faint { position: absolute; left: 30px; top: 30px; width: 450px; height: 370px;
    background: linear-gradient(180deg, rgba(0,140,0,0.18), rgba(0,120,0,0.22));
    border-radius: 200px 200px 0 0; }
  .statement { position: absolute; left: 41px; top: 62px; width: 456px; font-family: "PT Sans", sans-serif;
    color: var(--green-ink); }
  .statement h2 { font-size: 15px; font-weight: 400; margin-bottom: 4px; }
  .statement p { font-size: 16px; line-height: 32px; text-align: justify; text-align-last: left; }
  .statement .signoff { text-align: right; text-align-last: right; font-weight: 700; font-size: 16px; }

  .back-badge { position: absolute; left: 40px; top: 421px; width: 466px; height: 88px; background: var(--white); }
  .back-badge .tagline { position: absolute; left: 10px; top: 12px; font-size: 25px; line-height: 1; }
  .back-badge .site { position: absolute; left: 10px; top: 55px; font-size: 22px; line-height: 1; }
  .back-badge .brand-box { left: 315px; top: 10px; width: 137px; height: 68px; padding: 4px 6px; }
  .back-badge .brand-row { font-size: 10px; line-height: 13px; }
  .back-badge .brand-row .brand-first { font-size: 12px; }
  .back-badge .brand-name { font-size: 23px; line-height: 27px; }
  .back-badge .brand-office { font-size: 8px; line-height: 12px; }

  .stamp-box { position: absolute; left: 807px; top: 48px; width: 139px; height: 125px; border: 1px solid var(--rule); }
  .address-lines { position: absolute; left: 594px; top: 0; width: 352px; height: 537px; }
</style>
</head>
<body>
<main class="canvas">

  <section class="card card--front">
    <div class="front-field"></div>
    <div class="capitol-photo" role="img" aria-label="Green-tinted photo of the state capitol dome"></div>
    <h1 class="headline headline--made">PROMISES MADE</h1>
    <p class="headline headline--kept">PROMISES KEPT</p>
    <p class="promise-lead">Again I Promise to</p>
    <ul class="promise-list">
      <li>continue to advocate for limited government</li>
      <li>advocate for educational choice</li>
      <li>promote fiscal responsibility, transparency, and accountability.</li>
      <li>take seriously my pledge to protect individual and economic liberty.</li>
    </ul>
    <div class="candidate-photo" role="img" aria-label="Portrait of the candidate in a blue shirt and tie, arms crossed"></div>
    <p class="tagline">Let’s Finish What We Started</p>
    <p class="site">www.DaltonPierceHD42.example</p>
    <div class="brand-box">
      <span class="brand-row"><span class="brand-kicker">Re-Elect</span><span class="brand-first">DALTON</span></span>
      <span class="brand-name">PIERCE</span>
      <span class="brand-office">Utah House of Representatives</span>
    </div>
  </section>

  <section class="card card--back">
    <div class="back-field"></div>
    <div class="capitol-faint" role="img" aria-label="Faint capitol building backdrop"></div>
    <article class="statement">
      <h2>Principled Conservative</h2>
      <p>I am committed to my oath to uphold the U.S. Constitution and Utah Constitution. As an attorney who has studied these documents, I understand the principles of federalism and of our republican form of government. I also understand that big government is a threat to our freedoms, even at the state and local levels. I have a record of sponsoring and supporting legislation that makes government more efficient and less burdensome.</p>
      <p class="signoff">- Dalton Pierce</p>
    </article>
    <div class="back-badge">
      <p class="tagline">Let’s Finish What We Started</p>
      <p class="site">www.DaltonPierceHD42.example</p>
      <div class="brand-box">
        <span class="brand-row"><span class="brand-kicker">Re-Elect</span><span class="brand-first">DALTON</span></span>
        <span class="brand-name">PIERCE</span>
        <span class="brand-office">Utah House of Representatives</span>
      </div>
    </div>
    <div class="stamp-box"></div>
    <svg class="address-lines" viewBox="0 0 352 537" aria-hidden="true">
      <g stroke="#9a9a9a" stroke-width="1">
        <line x1="0" y1="231" x2="352" y2="231"/>
        <line x1="0" y1="276" x2="352" y2="276"/>
        <line x1="0" y1="320" x2="352" y2="320"/>
        <line x1="0" y1="363" x2="352" y2="363"/>
        <line x1="0" y1="405" x2="352" y2="405"/>
        <line x1="0" y1="457" x2="352" y2="457"/>
      </g>
    </svg>
  </section>

</main>
</body>
</html>
```